Banner Ad Design Project: Image banner for new website

Hi,

we need an image banner for a new website we just launched. The image banner should come in the formats 728x90 and 300x250.

The website the banner should advertise is http://www.vellora-tonebox.com/ .

We leave it up to your experience to find the best text and to obtain a great clickrate. Banner should be CATCHY and MOTIVATE people to enter. We do not want to include our current "logo". Will require all design files and fonts.

Best regards,
Brendan

```html
<!DOCTYPE html>
<html lang="en">
<head>
<meta charset="utf-8">
<title>Vellora Tonebox – Banner Set</title>
<link href="https://fonts.googleapis.com/css2?family=PT+Sans:wght@700&family=Archivo+Black&display=swap" rel="stylesheet">
<style>
  :root{
    --stage:#ececec;
    --white:#ffffff;
    --ink-shadow:rgba(0,0,0,.75);
    --green:#86c540; --green-dark:#2f7d12; --green-btn:#5fb82a;
    --sky:#22d8ff;  --sky-btn:#27bff0;
    --teal:#27e6f2; --teal-btn:#14c9d8;
    --amber:#ff9b1c; --amber-btn:#f7891a;
    --tag:#4b5560; --tag-text:#c9d1d8;
    --speaker:#2a2d31; --speaker-edge:#bfc3c7;
  }
  *{margin:0;padding:0;box-sizing:border-box}
  html,body{width:1200px;height:900px;overflow:hidden}
  body{background:var(--stage);font-family:"PT Sans",Arial,sans-serif;position:relative}

  .banner{position:absolute;overflow:hidden;color:var(--white);box-shadow:0 4px 10px rgba(0,0,0,.35)}
  .banner__scene{position:absolute;inset:0}
  .theme-forest .banner__scene{background:linear-gradient(90deg,#0d2a06,#3b8a12 25%,#a7d84c 45%,#245e0a 70%,#7bbd2a 100%)}
  .theme-reeds  .banner__scene{background:linear-gradient(90deg,#1d5f9a,#f1a040 30%,#2aa4e8 55%,#e8b070 75%,#1f6fb0)}
  .theme-water  .banner__scene{background:linear-gradient(90deg,#062a3a,#0a7fa0 30%,#12b9d4 50%,#053a58 75%,#0b6a8c)}
  .theme-autumn .banner__scene{background:linear-gradient(90deg,#3a1a02,#d28a16 30%,#140b02 55%,#e09a24 75%,#5a2a04)}

  .speakers{position:absolute;border-radius:4px;background:linear-gradient(90deg,var(--speaker),#55595e 50%,var(--speaker));border:2px solid var(--speaker-edge)}

  .headline{position:absolute;font-weight:700;text-shadow:0 2px 4px var(--ink-shadow);line-height:1.15;text-align:center;white-space:nowrap}
  .url{position:absolute;font-weight:700;font-size:15px;text-shadow:0 1px 3px var(--ink-shadow);text-align:center;white-space:nowrap}
  .theme-forest .accent{color:var(--green)}
  .theme-reeds  .accent{color:var(--sky)}
  .theme-water  .accent{color:var(--teal)}
  .theme-autumn .accent{color:var(--amber)}

  .play{position:absolute;display:flex;align-items:center;justify-content:space-between;padding:0 4px 0 14px;border-radius:6px;
        font-family:"Archivo Black",Arial,sans-serif;font-size:16px;color:var(--white);text-shadow:0 1px 2px rgba(0,0,0,.6);
        border:1px solid rgba(255,255,255,.55);box-shadow:0 0 8px rgba(0,0,0,.5)}
  .theme-forest .play{background:linear-gradient(#8edc4a,var(--green-btn) 50%,var(--green-dark))}
  .theme-reeds  .play{background:linear-gradient(#8fe9ff,var(--sky-btn) 50%,#1082c4)}
  .theme-water  .play{background:linear-gradient(#7ff6ff,var(--teal-btn) 50%,#08889a)}
  .theme-autumn .play{background:linear-gradient(#ffc46a,var(--amber-btn) 50%,#c35a06)}
  .play svg{flex:none}

  .free-tag{position:absolute;width:64px;height:24px;border-radius:4px;background:linear-gradient(#6a747e,var(--tag));border:1px solid #9aa3ab;
            font-family:"Archivo Black",Arial,sans-serif;font-size:13px;color:var(--tag-text);display:flex;align-items:center;justify-content:center;letter-spacing:.5px}

  /* leaderboard 728x90 */
  .leaderboard{left:236px;width:728px;height:90px}
  .leaderboard .speakers{top:4px;height:82px;width:32px}
  .leaderboard .speakers.s1{left:8px;width:34px}
  .leaderboard .speakers.s2{left:58px}
  .leaderboard .headline{left:66px;width:474px;top:24px;font-size:27px}
  .leaderboard .url{left:66px;width:474px;top:56px}
  .leaderboard .play{left:541px;top:18px;width:178px;height:42px}
  .leaderboard .free-tag{left:652px;top:66px}

  /* rectangle 300x250 */
  .rectangle{top:486px;width:272px;height:226px}
  .rectangle .speakers.s1{left:168px;top:150px;width:28px;height:70px}
  .rectangle .speakers.s2{left:224px;top:126px;width:42px;height:96px}
  .rectangle .headline{left:0;width:272px;top:52px;font-size:23px}
  .rectangle .play{left:58px;top:130px;width:160px;height:36px;font-size:14px}
  .rectangle .url{left:0;width:272px;top:191px;font-size:14px}
  .rectangle .free-tag{left:18px;top:18px;transform:rotate(-18deg);width:60px}
  .rectangle.tall-copy .headline{top:24px}
</style>
</head>
<body>

<section class="banner leaderboard theme-forest" style="top:36px">
  <div class="banner__scene" role="img" aria-label="Blurred green forest backdrop"></div>
  <div class="speakers s1" role="img" aria-label="Loudspeaker"></div>
  <div class="speakers s2" role="img" aria-label="Loudspeaker"></div>
  <p class="headline">Listen online to <span class="accent">relaxing</span> sounds</p>
  <p class="url">www.vellora-tonebox.com</p>
  <a class="play">PLAY NOW<svg width="34" height="34" viewBox="0 0 34 34"><circle cx="17" cy="17" r="16" fill="#555b61" stroke="#d7dbde" stroke-width="2"/><path d="M13 10l11 7-11 7z" fill="#fff"/></svg></a>
  <span class="free-tag">FREE</span>
</section>

<section class="banner leaderboard theme-reeds" style="top:140px">
  <div class="banner__scene" role="img" aria-label="Blurred reeds against blue water"></div>
  <div class="speakers s1" role="img" aria-label="Loudspeaker"></div>
  <div class="speakers s2" role="img" aria-label="Loudspeaker"></div>
  <p class="headline">Download <span class="accent">free</span> audio backgrounds</p>
  <p class="url">www.vellora-tonebox.com</p>
  <a class="play">PLAY NOW<svg width="34" height="34" viewBox="0 0 34 34"><circle cx="17" cy="17" r="16" fill="#555b61" stroke="#d7dbde" stroke-width="2"/><path d="M13 10l11 7-11 7z" fill="#fff"/></svg></a>
  <span class="free-tag">FREE</span>
</section>

<section class="banner leaderboard theme-water" style="top:244px">
  <div class="banner__scene" role="img" aria-label="Blurred teal underwater scene"></div>
  <div class="speakers s1" role="img" aria-label="Loudspeaker"></div>
  <div class="speakers s2" role="img" aria-label="Loudspeaker"></div>
  <p class="headline">Create <span class="accent">your own</span> audio atmosphere</p>
  <p class="url">www.vellora-tonebox.com</p>
  <a class="play">PLAY NOW<svg width="34" height="34" viewBox="0 0 34 34"><circle cx="17" cy="17" r="16" fill="#555b61" stroke="#d7dbde" stroke-width="2"/><path d="M13 10l11 7-11 7z" fill="#fff"/></svg></a>
  <span class="free-tag">FREE</span>
</section>

<section class="banner leaderboard theme-autumn" style="top:350px">
  <div class="banner__scene" role="img" aria-label="Blurred autumn foliage"></div>
  <div class="speakers s1" role="img" aria-label="Loudspeaker"></div>
  <div class="speakers s2" role="img" aria-label="Loudspeaker"></div>
  <p class="headline">Free online <span class="accent">ambient</span> sound mixer</p>
  <p class="url">www.vellora-tonebox.com</p>
  <a class="play">PLAY NOW<svg width="34" height="34" viewBox="0 0 34 34"><circle cx="17" cy="17" r="16" fill="#555b61" stroke="#d7dbde" stroke-width="2"/><path d="M13 10l11 7-11 7z" fill="#fff"/></svg></a>
  <span class="free-tag">FREE</span>
</section>

<section class="banner rectangle theme-forest" style="left:34px">
  <div class="banner__scene" role="img" aria-label="Blurred green forest backdrop"></div>
  <span class="free-tag">FREE</span>
  <p class="headline">Listen online to<br><span class="accent">relaxing</span> sounds</p>
  <div class="speakers s1" role="img" aria-label="Loudspeaker"></div>
  <div class="speakers s2" role="img" aria-label="Loudspeaker"></div>
  <a class="play">PLAY NOW<svg width="30" height="30" viewBox="0 0 34 34"><circle cx="17" cy="17" r="16" fill="#555b61" stroke="#d7dbde" stroke-width="2"/><path d="M13 10l11 7-11 7z" fill="#fff"/></svg></a>
  <p class="url">www.vellora-tonebox.com</p>
</section>

<section class="banner rectangle theme-reeds" style="left:320px">
  <div class="banner__scene" role="img" aria-label="Blurred reeds against blue water"></div>
  <span class="free-tag">FREE</span>
  <p class="headline">Download <span class="accent">free</span><br>audio backgrounds</p>
  <div class="speakers s1" role="img" aria-label="Loudspeaker"></div>
  <div class="speakers s2" role="img" aria-label="Loudspeaker"></div>
  <a class="play">PLAY NOW<svg width="30" height="30" viewBox="0 0 34 34"><circle cx="17" cy="17" r="16" fill="#555b61" stroke="#d7dbde" stroke-width="2"/><path d="M13 10l11 7-11 7z" fill="#fff"/></svg></a>
  <p class="url">www.vellora-tonebox.com</p>
</section>

<section class="banner rectangle theme-water" style="left:607px">
  <div class="banner__scene" role="img" aria-label="Blurred teal underwater scene"></div>
  <span class="free-tag">FREE</span>
  <p class="headline">Create <span class="accent">your own</span><br>audio atmosphere</p>
  <div class="speakers s1" role="img" aria-label="Loudspeaker"></div>
  <div class="speakers s2" role="img" aria-label="Loudspeaker"></div>
  <a class="play">PLAY NOW<svg width="30" height="30" viewBox="0 0 34 34"><circle cx="17" cy="17" r="16" fill="#555b61" stroke="#d7dbde" stroke-width="2"/><path d="M13 10l11 7-11 7z" fill="#fff"/></svg></a>
  <p class="url">www.vellora-tonebox.com</p>
</section>

<section class="banner rectangle tall-copy theme-autumn" style="left:893px">
  <div class="banner__scene" role="img" aria-label="Blurred autumn foliage"></div>
  <span class="free-tag">FREE</span>
  <p class="headline">Free online<br><span class="accent">ambient sound</span><br>mixer</p>
  <div class="speakers s1" role="img" aria-label="Loudspeaker"></div>
  <div class="speakers s2" role="img" aria-label="Loudspeaker"></div>
  <a class="play">PLAY NOW<svg width="30" height="30" viewBox="0 0 34 34"><circle cx="17" cy="17" r="16" fill="#555b61" stroke="#d7dbde" stroke-width="2"/><path d="M13 10l11 7-11 7z" fill="#fff"/></svg></a>
  <p class="url">www.vellora-tonebox.com</p>
</section>

</body>
</html>
```